Letterhead and business card design

We have recently had a logo designed by tarnvalehub. now we need a corporate identity with business card and lettehead design.

Target Market(s)

law firms corporates

Industry/Entity Type

Business

Requirements
Should not have
• cheesy detecive stuff like magnifying glasses etxcc

```html
<!DOCTYPE html>
<html lang="en">
<head>
<meta charset="utf-8">
<title>Hallbrook &amp; Veyne — Letterhead</title>
<link rel="stylesheet" href="https://fonts.googleapis.com/css2?family=Questrial&display=swap">
<style>
  :root {
    --backdrop: #e4e4e4;
    --paper: #fbfbfb;
    --ink: #7a7a7a;
    --ink-soft: #9a9a9a;
    --rule: #a8a8a8;
    --tab: #a3a3a3;
  }
  html, body {
    margin: 0;
    width: 1200px;
    height: 968px;
    overflow: hidden;
    background: var(--backdrop);
  }
  .letterhead {
    position: absolute;
    left: 282px;
    top: 34px;
    width: 636px;
    height: 900px;
    background: var(--paper);
    box-shadow: 0 2px 10px rgba(0,0,0,0.10);
  }
  .fold-tab {
    position: absolute;
    width: 8px;
    height: 28px;
    background: var(--tab);
  }
  .fold-tab--left { left: 0; top: 40px; }
  .fold-tab--right { right: 0; top: 300px; }

  .brand {
    position: absolute;
    top: 84px;
    left: 0;
    right: 0;
    text-align: center;
  }
  .brand__name {
    font-family: "Questrial", sans-serif;
    font-weight: 400;
    font-size: 26px;
    letter-spacing: 1px;
    color: var(--ink);
    margin: 0;
    line-height: 1;
  }

  .footer {
    position: absolute;
    left: 60px;
    right: 60px;
    bottom: 60px;
    font-family: "Questrial", sans-serif;
    color: var(--ink-soft);
  }
  .footer__contacts {
    display: flex;
    align-items: center;
    gap: 18px;
    font-size: 11px;
    line-height: 1.45;
  }
  .footer__divider {
    width: 1px;
    height: 24px;
    background: var(--rule);
  }
  .contact-block { font-style: normal; }
  .contact-line {
    display: flex;
    align-items: center;
    gap: 6px;
  }
  .contact-line svg { width: 9px; height: 9px; fill: var(--ink-soft); }
  .footer__notice {
    margin: 12px 0 0;
    font-size: 8.5px;
    line-height: 1.4;
    text-align: center;
  }
</style>
</head>
<body>
  <main class="letterhead">
    <span class="fold-tab fold-tab--left"></span>
    <span class="fold-tab fold-tab--right"></span>

    <header class="brand">
      <h1 class="brand__name">Hallbrook &amp; Veyne</h1>
    </header>

    <footer class="footer">
      <div class="footer__contacts">
        <address class="contact-block">
          PO Box 918, Harbourline Road<br>Kelbourne, New Zealand
        </address>
        <span class="footer__divider"></span>
        <div class="contact-block">
          <div class="contact-line">
            <svg viewBox="0 0 10 10"><rect x="0" y="2" width="10" height="6" rx="1"/></svg>
            marc@veyneinquiries.co.nz
          </div>
          <div class="contact-line">
            <svg viewBox="0 0 10 10"><circle cx="5" cy="5" r="4.5"/></svg>
            www.veyneinquiries.co.nz
          </div>
        </div>
        <span class="footer__divider"></span>
        <div class="contact-block">
          <div class="contact-line">
            <svg viewBox="0 0 10 10"><rect x="1" y="1" width="8" height="8" rx="1"/></svg>
            +64 9 555 0142
          </div>
          <div class="contact-line">
            <svg viewBox="0 0 10 10"><rect x="2.5" y="0.5" width="5" height="9" rx="1"/></svg>
            +64 9 555 0187
          </div>
        </div>
      </div>
      <p class="footer__notice">
        Government Licenced Private Investigator licence number 480326. Hallbrook and Veyne Inquiries Limited have no more authority<br>
        than that of an ordinary private citizen to require a reply to this correspondence.
      </p>
    </footer>
  </main>
</body>
</html>
```